Oxford Choir needs a concert poster!

22nd November is St Wendelin's Day, the Patron Saint of music. 100 years ago on that day, Rupert Calloway was born, famously dubbed the "greatest English composer since Marlowe". 50 years ago that day, three of the most prominent men in history died: this trifecta included theologian and author of 'Quelmor' R. P. Dunmore, philosopher and author of 'Silent Amber Shore' Peregrine Vostell, and one of America's most beloved presidents, Walter P. Hargrove.

In memory of these prominent figures of the 20th century, the Choir of St Oswin by the Tanner Row (the Parish Kirk of Fenwold) perform some of the world's best vocal music composed or inspired by these men. The playlist includes Calloway's 'Canticle for St Wendelin', G. F. Olbrich's 'Sieh, Vater, sieh', 'The Orchard' by Peregrine Vostell set to music by Percy Madden, and Clement Yardley' 'Hold her, sea, in quiet keeping', written specially for the memorial service of President Walter P Hargrove in Marlbury Grand Minster.

We are looking for a dramatic concert poster / or series of posters that encapsulate all these important aspects on this one day. Tickets will be set up on passgrabber.example - space for their logo will be needed.

22nd November 2013, 8pm
Radley Hall Oratory, Oxford
Choir of St Oswin by the Tanner Row
Giles Pemberton-Roe
Tickets: £5

Mostly students and staff from the Universities of Oxford and Whitfield, but also singers from local Oxfordshire choral societies who have a passion for singing and the repertoire. Local musical professionals and appreciators. Not really suitable for children. Cultured adults that support local artistic projects and go to live classical concerts. Higher-end readership. I would like to charge much more for the ticket prices (in order to reflect the quality of the performance) but Oxford is haemorrhaging quality concerts for very little, and the competition is fierce. This poster needs to stand out from the crowd of other events going on, and perhaps be coupled with an inventive marketing strategy.

• St Oswin by the Tanner Row logo
Passgrabber.example logo

My name prominently displayed

```html
<!DOCTYPE html>
<html lang="en">
<head>
<meta charset="utf-8">
<title>Choir of St Oswin by the Tanner Row – Concert Poster</title>
<link rel="stylesheet" href="https://fonts.googleapis.com/css2?family=Bree+Serif&family=Dosis:wght@500;600;700&family=Yellowtail&family=Italianno&display=swap">
<style>
  :root {
    --bg-deep: #0a0306;
    --name-pink: #ffd2d2;
    --director-pink: #f4a6c4;
    --neon-core: #f2ffff;
    --neon-glow: #3fd6d6;
    --date-red: #9a3030;
    --time-pink: #ffb3b3;
    --venue-teal: #6fb6b0;
    --ticket-red: #ff4a2a;
    --promo-blue: #2f7fd0;
    --cd-blue: #3a8bf0;
    --theme-pink: #e9b7b7;
    --rep-teal: #8cc8c2;
    --logo-ink: #e8e8e8;
    --footer-amber: #d86a1a;
  }
  html, body {
    margin: 0;
    padding: 0;
    width: 828px;
    height: 1200px;
    overflow: hidden;
    background: var(--bg-deep);
  }
  .poster {
    position: relative;
    width: 828px;
    height: 1200px;
    overflow: hidden;
    background: var(--bg-deep);
  }
  .backdrop {
    position: absolute;
    inset: 0;
    background:
      radial-gradient(ellipse 55% 22% at 40% 30%, rgba(216,32,14,0.55), transparent 70%),
      radial-gradient(ellipse 70% 28% at 62% 62%, rgba(216,32,14,0.45), transparent 70%),
      radial-gradient(ellipse 40% 45% at 88% 80%, rgba(200,25,10,0.35), transparent 70%),
      radial-gradient(ellipse 60% 30% at 30% 85%, rgba(120,10,8,0.4), transparent 70%),
      linear-gradient(180deg, #120408 0%, #1a0507 40%, #0c0305 100%);
  }
  .line {
    position: absolute;
    left: 0;
    width: 100%;
    text-align: center;
    margin: 0;
    white-space: nowrap;
    line-height: 1.15;
  }
  .director-name {
    top: 26px;
    font-family: "Bree Serif", serif;
    font-size: 31px;
    color: var(--name-pink);
  }
  .director-role {
    top: 68px;
    font-family: "Dosis", sans-serif;
    font-weight: 700;
    font-size: 22px;
    color: var(--director-pink);
  }
  .choir-title {
    font-family: "Yellowtail", cursive;
    color: var(--neon-core);
    text-shadow: 0 0 6px var(--neon-glow), 0 0 14px var(--neon-glow), 0 0 26px var(--neon-glow);
    letter-spacing: 2px;
    font-weight: 400;
  }
  .choir-title.first { top: 158px; font-size: 74px; }
  .choir-title.joiner { top: 252px; font-size: 66px; }
  .choir-title.last { top: 336px; font-size: 90px; }
  .event-date {
    top: 466px;
    font-family: "Italianno", cursive;
    font-size: 58px;
    color: var(--date-red);
    letter-spacing: 3px;
  }
  .event-time {
    top: 528px;
    font-family: "Dosis", sans-serif;
    font-weight: 700;
    font-size: 42px;
    color: var(--time-pink);
  }
  .event-venue {
    top: 588px;
    font-family: "Italianno", cursive;
    font-size: 60px;
    color: var(--venue-teal);
    letter-spacing: 3px;
  }
  .tickets {
    top: 690px;
    font-family: "Dosis", sans-serif;
    font-weight: 600;
    font-size: 25px;
    color: var(--ticket-red);
  }
  .promo {
    font-family: "Dosis", sans-serif;
    font-weight: 600;
    font-size: 24px;
    color: var(--promo-blue);
  }
  .promo.intro { top: 762px; }
  .promo.review { top: 814px; }
  .cd-title {
    top: 860px;
    font-family: "Dosis", sans-serif;
    font-weight: 600;
    font-size: 44px;
    color: var(--cd-blue);
  }
  .promo.price { top: 926px; }
  .theme {
    top: 984px;
    font-family: "Dosis", sans-serif;
    font-weight: 600;
    font-size: 19px;
    color: var(--theme-pink);
  }
  .repertoire {
    font-family: "Dosis", sans-serif;
    font-weight: 500;
    font-size: 18px;
    color: var(--rep-teal);
  }
  .repertoire.one { top: 1016px; }
  .repertoire.two { top: 1042px; }
  .partner-logos {
    position: absolute;
    left: 0;
    top: 1092px;
    width: 100%;
    display: flex;
    justify-content: center;
    gap: 64px;
  }
  .logo-mark {
    display: flex;
    align-items: center;
    gap: 10px;
    font-family: "Dosis", sans-serif;
    font-weight: 700;
    font-size: 20px;
    color: var(--logo-ink);
    white-space: nowrap;
  }
  .logo-mark svg { display: block; }
  .more-info {
    position: absolute;
    left: 8px;
    top: 1166px;
    margin: 0;
    font-family: "Dosis", sans-serif;
    font-weight: 600;
    font-size: 18px;
    color: var(--footer-amber);
    white-space: nowrap;
  }
</style>
</head>
<body>
<main class="poster">
  <div class="backdrop" role="img" aria-label="Dark photograph of rows of red theatre seats glowing in low light"></div>

  <p class="line director-name">Giles Pemberton-Roe</p>
  <p class="line director-role">director</p>

  <h1 class="line choir-title first">Choir of St Oswin</h1>
  <p class="line choir-title joiner">by the</p>
  <p class="line choir-title last">Tanner Row</p>

  <p class="line event-date">22nd November 2013</p>
  <p class="line event-time">8pm</p>
  <p class="line event-venue">Radley Hall Oratory, Oxford</p>

  <p class="line tickets">Tickets: £5 [from Passgrabber.example - to be set up]</p>

  <p class="line promo intro">Concert-goers will be able to buy the choir's</p>
  <p class="line promo review">latest 5-star reviewed CD</p>
  <p class="line cd-title">"The Thornbury Legacy"</p>
  <p class="line promo price">for just £8 (R.R.P. £12.95).</p>

  <p class="line theme">St Wendelin's Day: Calloway at 100 · Dunmore, Vostell &amp; Hargrove remembered</p>
  <p class="line repertoire one">Calloway – Canticle for St Wendelin · Olbrich – Sieh, Vater, sieh</p>
  <p class="line repertoire two">Madden – The Orchard · Yardley – Hold her, sea, in quiet keeping</p>

  <div class="partner-logos">
    <div class="logo-mark">
      <svg width="22" height="22" viewBox="0 0 22 22" aria-hidden="true"><circle cx="11" cy="11" r="10" fill="var(--logo-ink)"/></svg>
      <span>St Oswin by the Tanner Row</span>
    </div>
    <div class="logo-mark">
      <svg width="20" height="20" viewBox="0 0 20 20" aria-hidden="true"><rect width="20" height="20" fill="var(--logo-ink)"/></svg>
      <span>Passgrabber.example</span>
    </div>
  </div>

  <p class="more-info">[More information: www.gilespembertonroe.example and www.sotr.example]</p>
</main>
</body>
</html>
```